Blow Dry Bar Business Cards

These cards must be eye catching and modern.
You must be willing to work fast and make changes.

Winner will be offered other projects

Files 1 THIS IS THE STYLE CARDS I AM INTRESTED IN!!!
Please be creative, I am paying for my own eye catching design. I need files to be prisma press ready.

COLORS THAT ARE PAINTED INSIDE MY SHOP:
- - - http://www.brenwickcoatings.example/en/explore-colors/painter/color-selector.html?colors=4007-3C

- - - http://www.tarnellhues.example/color/paint-colors/quiet-harbor-d58-2

I want the business cards sleek and modern if you use the logo please correct imperfections. I added the part that says Blow Dry Bar (see website).
Do not be afraid to separate the blow dryer from the name to make the cards look like the file with the pink elephant.

SHOULD INCLUDE
*Blow Dryer (we are a blow dry bar not a salon we do not cut or color so do not include sheers of any kind)
*BUSINESS NAME: Simply Silken Waves - Blow Dry Bar (PLEASE SEE MY WEBSITE)
* Website: SIMPLYSILKENWAVES.EXAMPLE
*Phone number (555) 014-2763
Updates

Prisma press said it can be submitted in JPG

http://www.tarnellhues.example/color/paint-colors/quiet-harbor-d58-2 http://www.brenwickcoatings.example/en/explore-colors/painter/color-selector.html?colors=4007-3C ^^^^ These links will take you to the color paint that is painted inside my shop.

Target Market(s)

AGES 18 - 55 WOMEN
HIGH END MARKET

Industry/Entity Type

Salon

Requirements
Must have
• SEE COLOR EXAMPLE FILE
BLOW DRYER
UNIQUE
I LIKE THE CARD WITH THE PINK ELEPHANT THE BEST
Nice to have
• BE AS CREATIVE AND MODERN AS POSSIBLE DO NOT COPY ANY OF THE CARDS BELOW.
Should not have
• SCISSORS
PINK

```html
<!DOCTYPE html>
<html lang="en">
<head>
<meta charset="utf-8">
<title>Simply Silken Waves – Blow Dry Bar Business Card</title>
<link rel="stylesheet" href="https://fonts.googleapis.com/css2?family=Open+Sans:wght@400;600&family=Lora:wght@400&display=swap">
<style>
  :root {
    --stage: #ebe6e1;
    --card: #4a2f35;
    --card-deep: #3a2429;
    --sheen: #6a4b52;
    --teal: #5ec8cd;
    --ink-light: #f4eff0;
  }
  * { box-sizing: border-box; margin: 0; padding: 0; }
  html, body {
    width: 1200px;
    height: 1023px;
    overflow: hidden;
    background: var(--stage);
  }
  .sheet {
    width: 1200px;
    height: 1023px;
    display: flex;
    flex-direction: column;
    align-items: center;
    justify-content: center;
    gap: 70px;
  }
  .card {
    position: relative;
    width: 700px;
    height: 400px;
    border-radius: 28px;
    background: linear-gradient(135deg, var(--sheen) 0%, var(--card) 45%, var(--card-deep) 100%);
    box-shadow: 0 10px 24px rgba(40, 25, 28, 0.28);
    overflow: hidden;
  }

  /* Front */
  .front-brand {
    position: absolute;
    top: 110px;
    right: 70px;
    text-align: right;
    font-family: "Open Sans", sans-serif;
    color: var(--ink-light);
  }
  .front-brand .brand-row {
    display: flex;
    align-items: center;
    justify-content: flex-end;
    gap: 16px;
  }
  .front-brand .brand-dot {
    width: 26px;
    height: 26px;
    border-radius: 50%;
    background: var(--teal);
  }
  .front-brand .brand-name {
    font-size: 36px;
    font-weight: 400;
    letter-spacing: 0.5px;
  }
  .front-brand .brand-tagline {
    margin-top: 6px;
    font-size: 24px;
    font-weight: 400;
  }

  /* Back */
  .back-brand {
    position: absolute;
    top: 70px;
    right: 70px;
    display: flex;
    align-items: center;
    gap: 16px;
  }
  .back-brand .brand-name {
    font-family: "Lora", serif;
    font-size: 52px;
    font-weight: 400;
    color: var(--teal);
  }
  .back-brand .brand-dot {
    width: 30px;
    height: 30px;
    border-radius: 50%;
    background: var(--teal);
  }
  .contact {
    position: absolute;
    left: 60px;
    bottom: 60px;
    font-family: "Open Sans", sans-serif;
    color: var(--ink-light);
    font-size: 21px;
    line-height: 1.45;
  }
  .contact .address { margin-bottom: 18px; }
  .contact .line {
    display: flex;
    align-items: center;
    gap: 12px;
  }
  .contact .icon { width: 20px; height: 20px; flex: none; }
  .contact .web { letter-spacing: 0.5px; }
</style>
</head>
<body>
<main class="sheet">
  <section class="card card-front">
    <div class="front-brand">
      <div class="brand-row">
        <span class="brand-dot"></span>
        <span class="brand-name">Simply Silken Waves</span>
      </div>
      <div class="brand-tagline">Blow Dry Bar</div>
    </div>
  </section>

  <section class="card card-back">
    <div class="back-brand">
      <span class="brand-name">Silken Waves</span>
      <span class="brand-dot"></span>
    </div>
    <div class="contact">
      <p class="address">482 Marlow Bend Drive Suite 7 Fernhaven,<br>texas 70001</p>
      <p class="line">
        <svg class="icon" viewBox="0 0 24 24" aria-hidden="true">
          <path fill="#5ec8cd" d="M6.6 10.8a15.1 15.1 0 0 0 6.6 6.6l2.2-2.2a1 1 0 0 1 1-.25 11.4 11.4 0 0 0 3.6.57 1 1 0 0 1 1 1V20a1 1 0 0 1-1 1A17 17 0 0 1 3 4a1 1 0 0 1 1-1h3.5a1 1 0 0 1 1 1c0 1.25.2 2.45.57 3.57a1 1 0 0 1-.25 1z"/>
        </svg>
        <span>(555) 014-2763</span>
      </p>
      <p class="line">
        <svg class="icon" viewBox="0 0 24 24" aria-hidden="true">
          <circle cx="12" cy="12" r="9" fill="none" stroke="#5ec8cd" stroke-width="2"/>
          <path d="M3 12h18M12 3c3 3 3 15 0 18M12 3c-3 3-3 15 0 18" fill="none" stroke="#5ec8cd" stroke-width="1.6"/>
        </svg>
        <span class="web">WWW.SIMPLYSILKENWAVES.EXAMPLE</span>
      </p>
    </div>
  </section>
</main>
</body>
</html>
```